School Signage

I am wanting designs for signs completed that prompt students of the school requirements for hats, preparation and play.

I've uploaded rough examples of what we're after, but we would like them stylised and better than the example, including:
- A stylised logo/graphic for the 'Wallumba 1, 2, 3'
- Clear, crisp signage for the words.
- Graphics that reinforce the message of the sign.

We're after three signs:
- One that will be located on the oval to prompt hat use.
- One that will be near the entry prompting the morning routine (please make this one landscape with instructions for 'on time' on one side, and 'late' on the other).
- One that will be located within the school prompting readiness for class.

```html
<!DOCTYPE html>
<html lang="en">
<head>
<meta charset="utf-8">
<title>Wallumba State High – School Signage</title>
<link rel="stylesheet" href="https://fonts.googleapis.com/css2?family=Montserrat:wght@400;500;600;700;800&display=swap">
<style>
  :root{
    --green:#0b4a0c;
    --yellow:#ffe500;
    --white:#ffffff;
    --board:#c8c8c8;
    --ink:#111111;
  }
  *{box-sizing:border-box;margin:0;padding:0}
  html,body{width:915px;height:1200px;overflow:hidden;background:var(--board)}
  body{position:relative;font-family:"Montserrat",Arial,sans-serif;color:var(--ink)}

  .sign-label{position:absolute;font-size:24px;font-weight:500;letter-spacing:1px;color:var(--green);transform:translateX(-50%);white-space:nowrap}

  .sign{position:absolute;width:366px;height:517px;background:var(--white);box-shadow:0 10px 28px rgba(0,0,0,.22);overflow:hidden}
  .sign--hats{left:81px;top:71px}
  .sign--routine{left:468px;top:71px}
  .sign--ready{left:81px;top:611px;background:var(--green)}
  .sign--ready-oval{left:468px;top:611px;background:none;box-shadow:none;overflow:visible}
  .oval-shape{position:absolute;left:1px;top:4px;width:363px;height:510px;border-radius:50%;background:var(--green);box-shadow:0 10px 28px rgba(0,0,0,.22)}

  /* header band */
  .header{position:absolute;left:0;top:0;width:366px;height:117px}
  .header svg{position:absolute;left:0;top:0}
  .header-title{position:absolute;left:25px;color:var(--yellow);font-weight:800;line-height:1;white-space:nowrap}
  .header-title--one{top:36px;font-size:42px;letter-spacing:-1.6px}
  .header-title--two{top:23px;font-size:28px;line-height:34px;letter-spacing:-1.1px}

  .school-mark{position:absolute;text-align:center;color:var(--green);font-weight:700;line-height:1.15;display:flex;flex-direction:column;align-items:center;gap:4px}
  .school-mark .dot{width:10px;height:10px;border-radius:50%;background:var(--green)}
  .school-mark--head{left:250px;top:38px;width:100px;font-size:11px}
  .school-mark--dark{left:103px;top:58px;width:160px;font-size:13px;color:var(--yellow)}
  .school-mark--dark .dot{background:var(--yellow)}

  /* shared text */
  .lead{position:absolute;left:0;width:366px;text-align:center;color:var(--green);font-weight:800;letter-spacing:-.7px}
  .pill{position:absolute;background:var(--yellow);border-radius:4px;display:flex;align-items:center;justify-content:center;color:var(--ink);font-weight:500;letter-spacing:-.5px}

  /* hat sign steps */
  .step{position:absolute;left:46px;width:275px;height:62px;border:2px solid var(--yellow);border-radius:6px;background:var(--white)}
  .step-tab{position:absolute;right:-2px;top:-2px;width:29px;height:29px;background:var(--yellow);border-radius:0 6px 0 8px;display:flex;align-items:center;justify-content:center;font-weight:700;font-size:15px;color:var(--green)}
  .step-figure{position:absolute;top:8px;width:32px;height:44px;background:var(--green);border-radius:6px;opacity:.9}
  .step-word{position:absolute;top:14px;font-size:25px;font-weight:500;color:var(--ink)}

  /* routine boxes */
  .routine-box{position:absolute;width:217px;padding:10px 8px 10px 12px}
  .routine-box--on{left:25px;top:213px;height:132px;border:2px solid var(--yellow);border-radius:3px;background:var(--white)}
  .routine-box--late{left:128px;top:356px;height:136px;background:var(--green);border-radius:3px;color:var(--white)}
  .routine-heading{font-size:15px;font-weight:700;letter-spacing:-.4px;margin-bottom:7px;color:var(--green)}
  .routine-box--late .routine-heading{color:var(--yellow)}
  .routine-item{display:flex;gap:10px;align-items:flex-start;font-size:11.2px;line-height:13px;letter-spacing:-.35px;margin-bottom:8px}
  .routine-item b{font-weight:700}
  .routine-icon{flex:0 0 15px;height:15px;margin-top:-1px}
  .routine-icon--flat{background:var(--green);border-radius:2px}
  .routine-box--late .routine-icon--flat{background:var(--yellow)}

  .slogan{position:absolute;left:204px;top:222px;transform:rotate(-4deg);transform-origin:left top;font-size:15.5px;font-weight:800;color:var(--green);line-height:21px;letter-spacing:-.4px;white-space:nowrap}
  .slogan span{background:var(--yellow);padding:0 3px;border-radius:2px;display:inline-block;margin-bottom:1px}

  /* ready sign */
  .ready-title{position:absolute;left:0;top:138px;width:366px;text-align:center;color:var(--yellow);font-weight:800;font-size:25px;letter-spacing:-.8px}
  .ready-sub{position:absolute;left:0;top:174px;width:366px;text-align:center;color:var(--white);font-size:16.5px;font-weight:500}
  .ready-rule{position:absolute;left:77px;top:207px;width:211px;height:1px;background:var(--yellow);opacity:.7}
  .ready-question{position:absolute;left:0;top:218px;width:366px;text-align:center;color:var(--white);font-weight:700;font-size:18.5px;letter-spacing:-.6px}
  .check{position:absolute;left:82px;width:206px;height:46px;border:1.5px solid var(--yellow);border-radius:5px}
  .check-tab{position:absolute;right:-1.5px;top:-1.5px;width:22px;height:22px;background:var(--yellow);border-radius:0 5px 0 6px;display:flex;align-items:center;justify-content:center;font-weight:700;font-size:11.5px;color:var(--green)}
  .check-icon{position:absolute;left:14px;top:8px;width:44px;height:30px}
  .check-icon--flat{width:26px;left:24px;background:var(--white);border-radius:5px;opacity:.9}
  .check-text{position:absolute;left:70px;top:0;height:100%;display:flex;align-items:center;color:var(--white);font-size:12px;line-height:15px;font-weight:500}
</style>
</head>
<body>

<div class="sign-label" style="left:264px;top:30px">SIGN 01</div>
<div class="sign-label" style="left:651px;top:30px">SIGN 02</div>
<div class="sign-label" style="left:457px;top:1145px">SIGN 03</div>

<!-- Hats sign -->
<section class="sign sign--hats">
  <div class="header">
    <svg width="366" height="117" viewBox="0 0 366 117">
      <rect width="366" height="117" fill="var(--green)"/>
      <path d="M241 0 C228 40 244 92 273 117 L366 117 L366 0 Z" fill="var(--white)"/>
    </svg>
    <div class="header-title header-title--one">Integrity</div>
    <div class="school-mark school-mark--head"><span class="dot"></span><span>WALLUMBA<br>STATE HIGH</span></div>
  </div>

  <div class="lead" style="top:128px;font-size:20px;line-height:28px">We wear hats at Wallumba<br>when outdoors...</div>
  <div class="pill" style="left:46px;top:200px;width:275px;height:37px;font-size:18.5px">The Wallumba 1, 2, 3</div>

  <div class="step" style="top:257px">
    <div class="step-figure" role="img" aria-label="Figure of a student walking" style="left:58px"></div>
    <div class="step-word" style="left:108px">Walking</div>
    <div class="step-tab">01</div>
  </div>
  <div class="step" style="top:331px">
    <div class="step-figure" role="img" aria-label="Figure of a student sitting" style="left:70px"></div>
    <div class="step-word" style="left:121px">Sitting</div>
    <div class="step-tab">02</div>
  </div>
  <div class="step" style="top:404px">
    <div class="step-figure" role="img" aria-label="Figure of a student throwing a ball" style="left:62px"></div>
    <div class="step-word" style="left:114px">Playing</div>
    <div class="step-tab">03</div>
  </div>
</section>

<!-- Morning routine sign -->
<section class="sign sign--routine">
  <div class="header">
    <svg width="366" height="117" viewBox="0 0 366 117">
      <rect width="366" height="117" fill="var(--green)"/>
      <path d="M241 0 C228 40 244 92 273 117 L366 117 L366 0 Z" fill="var(--white)"/>
    </svg>
    <div class="header-title header-title--two">Exceed Your<br>Expectations</div>
    <div class="school-mark school-mark--head"><span class="dot"></span><span>WALLUMBA<br>STATE HIGH</span></div>
  </div>

  <div class="lead" style="top:129px;font-size:26px">Morning Routine</div>
  <div class="pill" style="left:78px;top:165px;width:210px;height:37px;font-size:18.5px">The Wallumba 1, 2, 3</div>

  <div class="routine-box routine-box--on">
    <div class="routine-heading">On Time:</div>
    <div class="routine-item">
      <svg class="routine-icon" viewBox="0 0 16 16"><circle cx="8" cy="8" r="6.6" fill="none" stroke="var(--green)" stroke-width="2"/><path d="M8 4.5V8l2.5 1.6" fill="none" stroke="var(--green)" stroke-width="1.6"/></svg>
      <span>1. Arrive before <b>8:30 AM</b></span>
    </div>
    <div class="routine-item">
      <span class="routine-icon routine-icon--flat" role="img" aria-label="Locker icon"></span>
      <span>2. <b>Drop bag at locker</b> and<br>collect learning materials</span>
    </div>
    <div class="routine-item">
      <span class="routine-icon routine-icon--flat" role="img" aria-label="Backpack icon"></span>
      <span>3. Arrive at Home Group<br>House Assembly before <b>8:40 AM</b></span>
    </div>
  </div>

  <div class="slogan"><span>Early is on Time,</span><br><span>on time is late</span></div>

  <div class="routine-box routine-box--late">
    <div class="routine-heading">Running Late:</div>
    <div class="routine-item">
      <svg class="routine-icon" viewBox="0 0 16 16"><circle cx="8" cy="8" r="6.6" fill="none" stroke="var(--yellow)" stroke-width="2"/><path d="M8 4.5V8l2.5 1.6" fill="none" stroke="var(--yellow)" stroke-width="1.6"/></svg>
      <span>1. Arrive before <b>8:30 AM</b></span>
    </div>
    <div class="routine-item">
      <span class="routine-icon routine-icon--flat" role="img" aria-label="Locker icon"></span>
      <span>2. <b>Drop bag at locker</b> and<br>collect learning materials</span>
    </div>
    <div class="routine-item">
      <span class="routine-icon routine-icon--flat" role="img" aria-label="Backpack icon"></span>
      <span>3. Arrive at Home Group<br>House Assembly before <b>8:40 AM</b></span>
    </div>
  </div>
</section>

<!-- Ready for class sign, rectangular -->
<section class="sign sign--ready">
  <div class="school-mark school-mark--dark"><span class="dot"></span><span>WALLUMBA<br>STATE HIGH</span></div>
  <div class="ready-title">Curiosity &amp; Drive</div>
  <div class="ready-sub">Wallumba Learner Values</div>
  <div class="ready-rule"></div>
  <div class="ready-question">Are you ready for class?</div>
  <div class="pill" style="left:82px;top:251px;width:206px;height:27px;font-size:14px">The Wallumba 1, 2, 3</div>

  <div class="check" style="top:293px">
    <svg class="check-icon" viewBox="0 0 44 30"><rect x="7" y="3" width="30" height="19" rx="1.5" fill="none" stroke="var(--white)" stroke-width="2.5"/><path d="M2 25h40l-2 3H4z" fill="var(--white)"/></svg>
    <div class="check-text">Laptop/workbook</div>
    <div class="check-tab">01</div>
  </div>
  <div class="check" style="top:347px">
    <div class="check-icon check-icon--flat" role="img" aria-label="Phone pouch"></div>
    <div class="check-text">Phone in Pouchr</div>
    <div class="check-tab">02</div>
  </div>
  <div class="check" style="top:402px">
    <div class="check-icon check-icon--flat" role="img" aria-label="School cap" style="width:38px;left:18px;border-radius:18px 18px 4px 4px"></div>
    <div class="check-text">Correct uniform<br>(including hat)</div>
    <div class="check-tab">03</div>
  </div>
</section>

<!-- Ready for class sign, oval -->
<section class="sign sign--ready-oval">
  <div class="oval-shape"></div>
  <div class="school-mark school-mark--dark"><span class="dot"></span><span>WALLUMBA<br>STATE HIGH</span></div>
  <div class="ready-title">Curiosity &amp; Drive</div>
  <div class="ready-sub">Wallumba Learner Values</div>
  <div class="ready-rule"></div>
  <div class="ready-question">Are you ready for class?</div>
  <div class="pill" style="left:82px;top:251px;width:206px;height:27px;font-size:14px">The Wallumba 1, 2, 3</div>

  <div class="check" style="top:293px">
    <svg class="check-icon" viewBox="0 0 44 30"><rect x="7" y="3" width="30" height="19" rx="1.5" fill="none" stroke="var(--white)" stroke-width="2.5"/><path d="M2 25h40l-2 3H4z" fill="var(--white)"/></svg>
    <div class="check-text">Laptop/workbook</div>
    <div class="check-tab">01</div>
  </div>
  <div class="check" style="top:347px">
    <div class="check-icon check-icon--flat" role="img" aria-label="Phone pouch"></div>
    <div class="check-text">Phone in Pouchr</div>
    <div class="check-tab">02</div>
  </div>
  <div class="check" style="top:402px">
    <div class="check-icon check-icon--flat" role="img" aria-label="School cap" style="width:38px;left:18px;border-radius:18px 18px 4px 4px"></div>
    <div class="check-text">Correct uniform<br>(including hat)</div>
    <div class="check-tab">03</div>
  </div>
</section>

</body>
</html>
```